Web site - 5-8 page

We are a small, fresh pasta business called The Noodle Lark located in suburbs of Sacramento, CA. We sell our pasta, ravioli, meatballs and sauce at farmer's markets, events, and soon in our café & marketplace. (Jan 2014) . We also provide catering services. The site needs to communicate FRESH, local, no preservatives, artisan quality pasta. We offer vegetarian, vegan and gluten free products as well.

We would like a web site using our logos and colors to feature what we do, and where people can come buy it. A page to our standard take and make items/menu, our seasonal take and make menu, our catering menu, our new hot food café menu.

We want a page that we can update with "Where can you find The Noodle Lark"
A "specials page" and a page they can order from that they choose the location to pick it up or in the delivery area we deliver to them.
A page with photo's and referrals, testimony, comments, about us, etc. Maybe a page for recipes.
We need to update the events/find us page all the time, weekly, so it needs to be easy for us to go in and do that. We are Window's (not MAC) users if that makes a difference or not, not sure.

Ideally, the same person(s) that make the website would also do a separate project creating our catering and hot food menu brochure/layout and recipe cards

Reason: allow enough time for good quality work

I would like to see the landing page have the pasta shapes/sizes element that is found in the refrigerator wrap, the wrap on the trailer, and the menu - see photo and uploads. It's used as a banner or as a background, bright green.

                                   

 

Would like visitors to be able to "like" me or follow me from my web page. A button or a link?

                                        http://www.brightpantry-example.com/our-food/

Really like the layout of this site. More grocery oriented than café, but we are a take and make marketplace as well as a Panini salads and hot pasta menu for lunch.

Please add Café + Marketplace to headers. Our logo is good but we are now adding a café element and a fresh marketplace, se we need to communicate what we are/what we do. We think adding Café + Marketplace as a descriptor will help. Any ideas, feel free to put your own spin on it. Thank you!!

The designs are good...thanks to everyone!

Reason: To allow for the many updates we have added. Good designs coming in, thank you!

Target Market(s)

#1, busy mom's, busy family's (FAST, Economical meals, no preservatives, local food)
#2 24-34 yr olds that want fresh, vegetarian, vegan or gluten free meal options (no preservatives, local food)
#3 Fresh pasta lovers - any age. The enjoyment of quality fresh pasta and a good meal experience sharing it with friends and family

Industry/Entity Type

Catering

Font styles to use
Other font styles liked:
• EideticNeoRegular, duffy

Colors
9bcb3c
f78f20
eb1f27

Requirements
Must have
• Address, phone, name, logo, colors
Fresh pasta, ravioli, sauce and meatballs in take and make convenient packages. Stress fresh, preservative free, local ingredients, cooks in 45 SECONDS to 3.5 minutes depending on the pasta cut.
FAST meal
Where to find us page - upcoming events
A "specials" page
A page for recipe, how to cook our pasta, how to freeze and store fresh pasta,
How to order online page
Nice to have
• Testimony, links to Facebook, twitter, etc. Place for photo's of product, recent events, customer comments on how they used the product to create their recipe.
Should not have
• No stock photo's of tomato's, no dried pasta images, no Italian flags. No cheesy old world Italian loo or feel. Think fresh, modern, FAST!

```html
<!DOCTYPE html>
<html lang="en">
<head>
<meta charset="utf-8">
<title>The Noodle Lark – Café + Marketplace</title>
<link rel="stylesheet" href="https://fonts.googleapis.com/css2?family=Open+Sans:wght@300;400;600;700&family=Lobster&family=Oswald:wght@500;700&display=swap">
<style>
:root{
  --green:#9bcb3c;
  --green-dark:#7fae27;
  --green-deep:#5f8a1c;
  --orange:#f78f20;
  --red:#eb1f27;
  --red-dark:#c8141b;
  --ink:#444;
  --muted:#888;
  --line:#e2e2e2;
  --paper:#ffffff;
  --footer:#f2f2f2;
}
*{box-sizing:border-box;margin:0;padding:0}
html,body{width:831px;height:1200px;overflow:hidden}
body{font-family:"Open Sans",Arial,sans-serif;color:var(--ink);background:var(--paper);position:relative;font-size:11px}
.sidebar{position:absolute;left:0;top:0;width:270px;height:1200px;background:linear-gradient(160deg,#a9d44b,var(--green) 45%,#8fc033)}
.brand{height:210px;display:flex;align-items:center;justify-content:center;gap:12px}
.brand-mark{width:22px;height:22px;border-radius:50%;background:var(--red)}
.brand-name{font-family:"Open Sans",sans-serif;font-weight:700;font-size:30px;color:var(--red);line-height:1.05;text-align:left}
.panel-red{background:var(--red);margin:0 14px;border:3px solid #fff;box-shadow:0 2px 4px rgba(0,0,0,.2)}
.panel-title{font-family:"Lobster",cursive;color:#fff;font-size:26px;padding:8px 18px 4px}
.products-list{list-style:none;padding:0 0 10px}
.products-list li{color:#fff;font-size:14px;padding:9px 22px;border-top:1px dashed rgba(255,255,255,.45)}
.quick-title{font-family:"Lobster",cursive;color:#fff;font-size:28px;text-shadow:0 2px 0 var(--green-deep);padding:26px 0 0 36px;height:80px}
.contact-title{font-family:"Lobster",cursive;color:#fff;font-size:28px;text-align:center;margin-top:16px;padding-bottom:10px;border-bottom:1px solid rgba(255,255,255,.5);margin-left:24px;margin-right:24px}
.contact-list{list-style:none;padding:16px 30px 0}
.contact-list li{display:flex;gap:12px;color:#fff;font-size:12.5px;line-height:1.45;margin-bottom:14px;align-items:flex-start}
.contact-list svg{flex:none;margin-top:2px}
.who{position:absolute;left:14px;right:14px;top:815px;bottom:0;border-bottom:none}
.who-title{text-align:center;font-size:26px;padding-top:10px}
.who p{color:#fff;font-size:10.5px;line-height:1.55;padding:6px 18px 0}
.main{position:absolute;left:277px;top:0;width:554px;height:1200px}
.topbar{height:36px;display:flex;align-items:center;justify-content:space-between;font-size:9.5px;color:var(--muted);padding:0 4px}
.toplinks{display:flex;gap:6px;align-items:center}
.social{display:flex;gap:4px}
.social span{width:13px;height:13px;border-radius:50%;background:var(--orange)}
.social span+span{background:#3b9fd8}
.call{text-align:right;line-height:1}
.call small{font-size:8.5px;color:var(--muted)}
.call strong{display:block;font-size:17px;color:var(--orange);font-weight:700}
.nav{height:36px;background:var(--green);display:flex;align-items:stretch;border-top:3px solid var(--green-dark)}
.nav a{color:#fff;text-decoration:none;font-weight:700;font-size:12.5px;padding:0 17px;display:flex;align-items:center;border-right:1px solid rgba(255,255,255,.4)}
.nav a:last-child{border-right:none;margin-left:auto}
.hero{position:relative;margin-top:8px;height:220px;background:radial-gradient(ellipse at 55% 60%,#e0592a 0%,#c9432a 35%,#e9b27a 70%,#f4e3c8 100%)}
.price-tag{position:absolute;left:70px;top:70px;background:var(--orange);color:#fff;font-family:"Oswald",sans-serif;font-weight:700;font-size:26px;line-height:1.05;padding:10px 18px 10px 24px;transform:rotate(-4deg)}
.price-tag span{display:block;font-size:22px}
.dots{position:absolute;right:12px;bottom:10px;display:flex;gap:6px}
.dots i{width:10px;height:10px;border-radius:50%;background:#fff;opacity:.7}
.dots i:first-child{background:var(--red);opacity:1}
.order{height:70px;margin-top:8px;border-top:2px solid var(--orange);border-bottom:1px solid var(--line);display:flex;align-items:center;gap:8px;padding:0 4px}
.order h2{font-size:15px;font-weight:400;color:var(--muted);margin-right:10px;position:absolute;top:240px}
.order-head{position:absolute;left:4px;top:302px;font-size:15px;color:#777;letter-spacing:.2px}
.order-head b{color:var(--orange);font-weight:400}
.order-row{display:flex;gap:10px;margin-top:34px;align-items:center;padding-left:4px}
.select{width:150px;height:24px;border:1px solid #ccc;background:#fff;font-size:9px;color:#999;display:flex;align-items:center;justify-content:space-between;padding:0 8px}
.select-short{width:170px}
.btn{background:var(--green);color:#fff;font-weight:600;font-size:11.5px;padding:6px 14px;border-radius:3px}
.products{position:relative;height:305px;margin-top:10px}
.tile{position:absolute;overflow:hidden}
.tile-photo{position:absolute;inset:0}
.tile-label{position:absolute;left:0;bottom:0;right:0;padding:6px 10px;font-family:"Oswald",sans-serif;font-weight:500;font-size:17px;color:var(--red);background:rgba(255,214,120,.92)}
.tile-pasta{left:0;top:0;width:276px;height:305px}
.tile-ravioli{left:284px;top:0;width:270px;height:148px}
.tile-sauce{left:284px;top:156px;width:270px;height:149px}
.tile-pasta .tile-photo{background:linear-gradient(135deg,#f3c95a,#e7a93a 55%,#d98d2a)}
.tile-ravioli .tile-photo{background:linear-gradient(135deg,#f6d98c,#eec36b)}
.tile-sauce .tile-photo{background:linear-gradient(135deg,#e9a77a,#c44a25 70%)}
.tile-ravioli .tile-label{top:55px;bottom:auto;right:auto;background:rgba(255,225,150,.95);font-size:18px}
.tile-sauce .tile-label{top:85px;bottom:auto;right:auto;background:var(--orange);color:#fff;font-size:15px}
.columns{display:flex;gap:24px;margin-top:16px;padding:0 4px}
.col{flex:1}
.col h3{font-weight:300;font-size:21px;color:#555;padding-bottom:8px;border-bottom:1px solid var(--line);margin-bottom:12px}
.quote{position:relative;padding:0 16px;margin-bottom:10px}
.quote p{color:#777;font-size:10.5px;line-height:1.6}
.quote-mark{position:absolute;font-size:46px;color:#ddd;font-family:Georgia,serif;line-height:1}
.quote-mark.open{left:-4px;top:-6px}
.quote-mark.close{right:-2px;bottom:-28px}
.by{color:var(--red);font-size:10.5px;margin:26px 0 30px 0}
.event{margin-bottom:12px}
.event h4{color:var(--red);font-size:10.5px;font-weight:400;line-height:1.5}
.event p{color:#777;font-size:10.5px;line-height:1.55}
.more{color:var(--red);font-size:10.5px;margin-top:6px}
.footer{position:absolute;left:0;right:0;top:1155px;height:32px;background:var(--footer);display:flex;align-items:center;justify-content:space-between;padding:0 10px;font-size:9.5px;color:var(--muted)}
.follow{display:flex;align-items:center;gap:5px}
.follow span{width:13px;height:13px;border-radius:50%;background:#bbb}
</style>
</head>
<body>

<aside class="sidebar">
  <div class="brand">
    <span class="brand-mark"></span>
    <div class="brand-name">The Noodle<br>Lark</div>
  </div>

  <section class="panel-red">
    <h2 class="panel-title">Our Products</h2>
    <ul class="products-list">
      <li>Lorem ipsum dolor</li>
      <li>Nam posuere</li>
      <li>Vitae posuere enim</li>
      <li>Duis laoreet et</li>
      <li>Suspendisse</li>
    </ul>
  </section>

  <h2 class="quick-title">Quick Contact</h2>

  <h3 class="contact-title">The Noodle Lark</h3>
  <ul class="contact-list">
    <li>
      <svg width="14" height="16" viewBox="0 0 14 16"><path d="M7 0a5.5 5.5 0 0 0-5.5 5.5C1.5 10 7 16 7 16s5.5-6 5.5-10.5A5.5 5.5 0 0 0 7 0z" fill="#fff"/><circle cx="7" cy="5.5" r="2" fill="#9bcb3c"/></svg>
      <span>48 Orchard Loop,<br>Maple Grove, CA 95600<br>(555) 014-2281</span>
    </li>
    <li>
      <svg width="14" height="14" viewBox="0 0 14 14"><path d="M3 0l3 3-1.6 2a8 8 0 0 0 4.6 4.6L11 8l3 3-2 2.5C6 13.5 0.5 8 .5 2z" fill="#fff"/></svg>
      <span>555-019-4410</span>
    </li>
    <li>
      <svg width="15" height="11" viewBox="0 0 15 11"><rect width="15" height="11" rx="1" fill="#fff"/><path d="M0.5 1l7 5 7-5" stroke="#9bcb3c" fill="none"/></svg>
      <span>hello@noodlelark-example.com</span>
    </li>
  </ul>

  <section class="panel-red who">
    <h2 class="panel-title who-title">Who we are</h2>
    <p>Welcome, The Noodle Lark specializes in fresh, artisan pasta. We are a café and farm to fork marketplace. We serve fresh made pasta, sandwiches, panini, homemade soups, salads and more. We can deliver your office lunch or party.</p>
    <p>Find our fare at local markets for fresh pasta, sauces, meats and cheeses that are produced locally. Our goal is to serve you healthy, preservative free, vegan, vegetarian and gluten free choices.</p>
    <p>New shop opening soon!</p>
  </section>
</aside>

<main class="main">
  <div class="topbar">
    <div class="toplinks">
      <span>The Kitchen</span>|<span>Restaurant &amp; Bar</span>|<span>Gift Cards</span>|<span>Join Our Newsletter</span>
      <div class="social"><span></span><span></span></div>
    </div>
    <div class="call"><small>Call us to order today</small><strong>555-019-4410</strong></div>
  </div>

  <nav class="nav">
    <a href="#">HOME</a>
    <a href="#">ABOUT US</a>
    <a href="#">OUR MENUS</a>
    <a href="#">CATERING</a>
    <a href="#">CONTACT US</a>
  </nav>

  <section class="hero" role="img" aria-label="Plate of fresh penne in tomato sauce with basil">
    <div class="price-tag">12 OZ. $6.00<span>&amp; Up</span></div>
    <div class="dots"><i></i><i></i><i></i></div>
  </section>

  <div class="order-head"><b>ORDER</b> YOUR TAKEAWAY ONLINE</div>
  <section class="order">
    <div class="order-row">
      <div class="select">Your postcode*<span>▾</span></div>
      <div class="select select-short">Choose your product<span>▾</span></div>
      <div class="btn">Find me to takeaway</div>
    </div>
  </section>

  <section class="products">
    <div class="tile tile-pasta">
      <div class="tile-photo" role="img" aria-label="Fresh pasta shapes and cuts"></div>
      <div class="tile-label">PASTA</div>
    </div>
    <div class="tile tile-ravioli">
      <div class="tile-photo" role="img" aria-label="Fresh ravioli"></div>
      <div class="tile-label">RAVIOLI</div>
    </div>
    <div class="tile tile-sauce">
      <div class="tile-photo" role="img" aria-label="Meatballs in tomato sauce"></div>
      <div class="tile-label">SAUCE AND MEATBALLS</div>
    </div>
  </section>

  <section class="columns">
    <div class="col">
      <h3>Clients Testimonials</h3>
      <div class="quote">
        <span class="quote-mark open">“</span>
        <p>Lorem ipsum dolor sit amet, consectetur adipiscing elit. Mauris rhoncus lacus dolor, non tempor purus commodo eu. Vivamus nibh justo, porta vel est eget, sagittis cursus nisi. Sed egestas mauris eget diam mattis pretium.</p>
        <span class="quote-mark close">”</span>
      </div>
      <div class="by">by - Miss Arden</div>
      <div class="quote">
        <span class="quote-mark open">“</span>
        <p>Lorem ipsum dolor sit amet, consectetur adipiscing elit. Mauris rhoncus lacus dolor, non tempor purus commodo eu. Vivamus nibh justo, porta vel est eget, sagittis cursus nisi. Sed egestas mauris eget diam mattis pretium.</p>
        <span class="quote-mark close">”</span>
      </div>
      <div class="by">by - Mrs. Hale</div>
    </div>

    <div class="col">
      <h3>Latest Events</h3>
      <div class="event">
        <h4>Vestibulum posuere metus eget lorem dapibus iaculis.</h4>
        <p>Sed egestas mauris eget diam mattis pretium. Ut consequat felis ut mauris hendrerit.</p>
      </div>
      <div class="event">
        <h4>Lorem ipsum dolor sit amet, consectetur.</h4>
        <p>In hac habitasse platea dictumst. Ut consequat felis ut mauris hendrerit.</p>
      </div>
      <div class="event">
        <h4>Vestibulum posuere metus eget lorem dapibus iaculis.</h4>
        <p>Sed egestas mauris eget diam mattis pretium. Ut consequat felis ut mauris hendrerit.</p>
      </div>
      <div class="event">
        <h4>Lorem ipsum dolor sit amet, consectetur.</h4>
        <p>In hac habitasse platea dictumst. Ut consequat felis ut mauris hendrerit.</p>
      </div>
      <div class="more">» Read More</div>
    </div>
  </section>

  <footer class="footer">
    <span>Copyright 2013, TheNoodleLark</span>
    <div class="follow">Follow Us <span></span><span></span></div>
  </footer>
</main>

</body>
</html>
```